Business Card Design Project

KRV Management Consulting, LLC is a management consulting firm focused on improving an organization’s health and wellness while enhancing company performance with an emphasis on winning in the marketplace, profitable growth, team building, culture enablement and innovation.

Industry/Entity Type

Business

```html
<!DOCTYPE html>
<html lang="en">
<head>
<meta charset="utf-8">
<title>KRV Management Consulting, LLC – Business Card</title>
<link rel="stylesheet" href="https://fonts.googleapis.com/css2?family=Cinzel:wght@400;500&family=Didact+Gothic&family=Lato:wght@400;700&display=swap">
<style>
  :root {
    --stage: #2a2a2a;
    --card: #1f1f1f;
    --ink: #f2f2f2;
    --muted: #9a9a9a;
    --green: #7ac143;
    --rule: #d8d8d8;
  }
  * { box-sizing: border-box; margin: 0; padding: 0; }
  html, body { width: 1200px; height: 900px; overflow: hidden; }
  body {
    background: var(--stage);
    font-family: "Didact Gothic", sans-serif;
    color: var(--ink);
    position: relative;
  }
  .card {
    position: absolute;
    left: 250px;
    width: 700px;
    height: 400px;
    background: var(--card);
    box-shadow: 0 8px 24px rgba(0,0,0,.45);
  }
  /* ---------- back ---------- */
  .card--back { top: 40px; padding: 22px 26px; }
  .back-title {
    font-family: "Cinzel", serif;
    color: var(--green);
    font-size: 25px;
    letter-spacing: 1px;
    text-align: center;
    margin-bottom: 6px;
  }
  .offer-box {
    position: relative;
    border: 1.5px solid var(--rule);
    padding: 18px 16px 10px;
    font-size: 12.5px;
    line-height: 1.35;
  }
  .tag {
    display: inline-block;
    background: var(--green);
    color: #fff;
    font-family: "Lato", sans-serif;
    font-size: 11px;
    padding: 1px 8px;
  }
  .offer-box > .tag { position: absolute; top: -9px; left: 16px; }
  .columns { display: flex; gap: 20px; }
  .columns ul { list-style: none; }
  .columns .col-left { flex: 0 0 260px; }
  .arrow { color: var(--green); margin-right: 6px; }
  .numbered { margin-top: 6px; }
  .num { color: var(--green); margin: 0 4px; }
  .purpose { margin-top: 8px; }
  .purpose-row { margin-top: 4px; word-spacing: 1px; }
  .purpose-row span { margin-right: 10px; }
  .impact-list {
    list-style: none;
    margin-top: 8px;
    font-size: 12.5px;
    line-height: 1.35;
  }
  .impact-list li::before { content: "•"; color: var(--green); margin-right: 8px; }
  /* ---------- front ---------- */
  .card--front { top: 470px; }
  .wordmark {
    position: absolute;
    left: 170px;
    top: 70px;
    font-family: "Lato", sans-serif;
    font-weight: 400;
    color: var(--ink);
  }
  .wordmark-short { display: block; font-size: 70px; line-height: 1; letter-spacing: 2px; margin-left: 10px; }
  .wordmark-long { display: block; font-size: 26px; letter-spacing: 2px; margin-top: 2px; }
  .holder {
    position: absolute;
    right: 430px;
    top: 260px;
    text-align: right;
  }
  .holder-name {
    font-family: "Cinzel", serif;
    color: var(--green);
    font-size: 24px;
  }
  .holder-role { font-family: "Lato", sans-serif; font-size: 19px; margin-top: 2px; }
  .divider {
    position: absolute;
    left: 292px;
    top: 258px;
    width: 2px;
    height: 76px;
    background: var(--ink);
  }
  .contact {
    position: absolute;
    left: 318px;
    top: 256px;
    list-style: none;
    font-family: "Lato", sans-serif;
    font-size: 19px;
    line-height: 1.45;
  }
  .contact li { display: flex; align-items: center; gap: 10px; }
  .contact svg { width: 16px; height: 16px; flex: none; }
</style>
</head>
<body>

<section class="card card--back">
  <h1 class="back-title">KRV Management Consulting, LLC</h1>
  <div class="offer-box">
    <span class="tag">SERVICE OFFERINGS:</span>
    <div class="columns">
      <ul class="col-left">
        <li><span class="arrow">&gt;</span>Organizational Health Services</li>
        <li><span class="arrow">&gt;</span>Company Turnaround Services</li>
        <li><span class="arrow">&gt;</span>Innovation Lab Establishment</li>
        <li><span class="arrow">&gt;</span>Enterprise Risk Management</li>
        <li><span class="arrow">&gt;</span>Business Strategy Development</li>
      </ul>
      <ul class="col-right">
        <li><span class="arrow">&gt;</span>Strategic Corporate Communication Strategy Development</li>
        <li><span class="arrow">&gt;</span>IT Strategy Development</li>
        <li><span class="arrow">&gt;</span>Complex Program and Project Management</li>
        <li><span class="arrow">&gt;</span>M&amp;A due diligence support</li>
        <li><span class="arrow">&gt;</span>Post-M&amp;A Integration Services including:</li>
      </ul>
    </div>
    <p class="numbered">
      <span class="num">1.</span>Change Management <span class="num">2.</span>Organization Design <span class="num">3.</span>Integrated Business Strategy Development<br>
      <span class="num">4.</span>IT Integration Strategy Development <span class="num">5.</span>Leadership Development
    </p>
    <div class="purpose">
      <span class="tag">Leading with Purpose</span>
      <p class="purpose-row">
        <span><span class="arrow">&gt;</span>Facilitating Change</span>
        <span><span class="arrow">&gt;</span>Solving Problems</span>
        <span><span class="arrow">&gt;</span>Building Trust</span>
        <span><span class="arrow">&gt;</span>Adding Humor</span>
        <span><span class="arrow">&gt;</span>Bringing Joy</span>
      </p>
    </div>
  </div>
  <ul class="impact-list">
    <li>Helping companies achieve change amid order and order amid change</li>
    <li>Helping companies develop a shared consciousness around their business strategies</li>
    <li>Helping companies Dance in the Hurricane</li>
    <li>Helping companies achieve profitable growth</li>
    <li>Enabling companies by effectively leveraging technology and innovation</li>
  </ul>
</section>

<section class="card card--front">
  <div class="wordmark">
    <span class="wordmark-short">KRV</span>
    <span class="wordmark-long">Management Consulting, LLC</span>
  </div>

  <div class="holder">
    <p class="holder-name">MARCO LINDQVIST</p>
    <p class="holder-role">Director</p>
  </div>

  <div class="divider"></div>

  <ul class="contact">
    <li>
      <svg viewBox="0 0 16 16" aria-hidden="true"><path d="M4 1.5l2.2 3-1.3 1.4c.8 1.8 2.2 3.3 4 4.2l1.4-1.3 3 2.2-1.1 2.3C7 13 3 9 1.7 2.6z" fill="var(--green)"/></svg>
      +330 5550-1482
    </li>
    <li>
      <svg viewBox="0 0 16 16" aria-hidden="true"><rect x="1.5" y="3.5" width="13" height="9" fill="none" stroke="var(--green)" stroke-width="1.4"/><path d="M1.5 3.5L8 9l6.5-5.5" fill="none" stroke="var(--green)" stroke-width="1.4"/></svg>
      KRVManagementConsulting,LLC.com
    </li>
    <li>
      <svg viewBox="0 0 16 16" aria-hidden="true"><g fill="none" stroke="var(--green)" stroke-width="1.2"><circle cx="8" cy="8" r="6.5"/><ellipse cx="8" cy="8" rx="2.8" ry="6.5"/><path d="M1.5 8h13M2.6 4.6h10.8M2.6 11.4h10.8"/></g></svg>
      KRVManagementConsulting,LLC.com
    </li>
  </ul>
</section>

</body>
</html>
```